New Business Card Design

We need a business card design for a new company based in Sydney called "Hearth and Ember". This is an online buisness which will have an online store providing imported homewares.
We are looking for something that is different, perhaps even in shape and using the logo that was designed by Pixel Meadow.

Attached document is a basic example I want to see more creative versions.

Target Market(s)

Homewares, Interior Design

Industry/Entity Type

Business

Contact Information for Business Card

Company Logo
Company Name
Industry area
Name
Position
Phone
Email
Website
Motto

Requirements
Must have
• Logo
Nice to have
• Social website logos - Friendlane, Glimmerly, Quipster, Boardwhim, Zumvo+

```html
<!DOCTYPE html>
<html lang="en">
<head>
<meta charset="utf-8">
<title>Hearth and Ember – Business Card</title>
<link rel="stylesheet" href="https://fonts.googleapis.com/css2?family=Open+Sans:wght@400;700&family=Satisfy&display=swap">
<style>
  :root {
    --page: #e6e7e9;
    --card: #f4f5f6;
    --card-edge: #b9bcc0;
    --band: #0b0b0b;
    --ink: #1c1c1c;
    --ink-soft: #3a3a3a;
    --muted: #b5b5b5;
    --white: #ffffff;
    --gold: #b07a2c;
    --gold-light: #e0b56a;
  }
  * { margin: 0; padding: 0; box-sizing: border-box; }
  html, body {
    width: 1200px; height: 970px; overflow: hidden;
    background: var(--page);
    font-family: "Open Sans", Arial, sans-serif;
  }
  .canvas { position: relative; width: 1200px; height: 970px; }
  .card {
    position: absolute; left: 100px; top: 207px;
    width: 1000px; height: 556px;
    border-radius: 34px; overflow: hidden;
    background: var(--card);
    border: 2px solid var(--card-edge);
    box-shadow: 0 18px 40px rgba(0,0,0,.12);
  }
  .band {
    position: absolute; left: 0; top: 0; width: 100%; height: 202px;
    background: var(--band);
  }
  .band-rule {
    position: absolute; left: 470px; right: 0; top: 202px; height: 4px;
    background: linear-gradient(90deg, var(--gold-light), var(--gold));
  }
  .brand-name {
    position: absolute; left: 23px; width: 480px; top: 118px;
    text-align: center; color: var(--white);
    font-size: 40px; font-weight: 400; line-height: 50px; letter-spacing: .5px;
  }
  .holder { position: absolute; left: 534px; top: 102px; }
  .holder-name {
    color: var(--white); font-weight: 700; font-size: 28px; line-height: 38px; letter-spacing: 1px;
  }
  .holder-role { color: var(--muted); font-size: 23px; line-height: 32px; }
  .contacts { position: absolute; left: 534px; top: 260px; list-style: none; }
  .contacts li {
    display: flex; align-items: center; gap: 10px;
    height: 38px; font-size: 24px; color: var(--ink);
  }
  .contacts svg { width: 22px; height: 22px; fill: var(--ink); flex: none; }
  .company { position: absolute; left: 23px; width: 480px; top: 380px; text-align: center; }
  .company-name, .company-trade { font-size: 24px; color: var(--ink-soft); line-height: 31px; }
  .social {
    position: absolute; left: 23px; width: 480px; top: 484px;
    display: flex; justify-content: center; gap: 10px; list-style: none;
    font-size: 13px; line-height: 20px; color: var(--ink);
  }
  .social li { display: flex; align-items: center; gap: 4px; }
  .social li::before {
    content: ""; width: 11px; height: 11px; border-radius: 50%; background: var(--ink);
  }
  .motto {
    position: absolute; left: 534px; top: 468px;
    font-family: "Satisfy", cursive; font-size: 36px; line-height: 48px; color: var(--ink);
    white-space: nowrap;
  }
</style>
</head>
<body>
<main class="canvas">
  <section class="card">
    <div class="band"></div>
    <div class="band-rule"></div>

    <div class="brand-name">Hearth and Ember</div>

    <div class="holder">
      <div class="holder-name">ELENA RUIZ WALSH</div>
      <div class="holder-role">Director / Designer</div>
    </div>

    <ul class="contacts">
      <li>
        <svg viewBox="0 0 24 24" aria-hidden="true"><path d="M6.6 10.8a15.5 15.5 0 0 0 6.6 6.6l2.2-2.2a1 1 0 0 1 1-.25 11.4 11.4 0 0 0 3.6.57 1 1 0 0 1 1 1V20a1 1 0 0 1-1 1A17 17 0 0 1 3 4a1 1 0 0 1 1-1h3.5a1 1 0 0 1 1 1c0 1.25.2 2.45.57 3.57a1 1 0 0 1-.25 1z"/></svg>
        +61 400 555 019
      </li>
      <li>
        <svg viewBox="0 0 24 24" aria-hidden="true"><path d="M2 5h20v14H2z M3.5 6.5 12 13l8.5-6.5" fill="none" stroke="#1c1c1c" stroke-width="2"/></svg>
        elena@hearthandember.com.au
      </li>
      <li>
        <svg viewBox="0 0 24 24" aria-hidden="true"><circle cx="12" cy="12" r="9" fill="none" stroke="#1c1c1c" stroke-width="2"/><path d="M3 12h18M12 3c3 3 3 15 0 18M12 3c-3 3-3 15 0 18" fill="none" stroke="#1c1c1c" stroke-width="1.6"/></svg>
        www.hearthandember.com.au
      </li>
    </ul>

    <div class="company">
      <div class="company-name">Hearth and Ember</div>
      <div class="company-trade">European &amp; Imported Homewares</div>
    </div>

    <ul class="social">
      <li>Friendlane</li>
      <li>Glimmerly</li>
      <li>Quipster</li>
      <li>Boardwhim</li>
      <li>Zumvo+</li>
    </ul>

    <div class="motto">Warmth for Every Room</div>
  </section>
</main>
</body>
</html>
```